WWW.VELTRONA.IT BUSINNES CARD

WE NEED A BUSINESS CARD . I HAVE A COMPANY IN ITALY NR 1 IN HAIR MEDICAL CARE AN HAIR REPLECEMENT . IN CARD I NEED WRITE WEB ADDRESS, MAIL , ADDRESS, TELEPHONE NUMBER , AND NAME
IN THE BACK SIDE I NEED MY DOCTOR LOGO .
MY WEB SITE IS WWW.VELTRONA.IT
Updates

Target Market(s)

CONSUMER B2C

Industry/Entity Type

Hair And Beauty

Contact Information for Business Card

I WANT A MEDICAL BUSINESS CARD.

Font styles to use
Other font styles liked:
• VERDANA

Colors
33a6d7
3176b5
85abd2
aedbee
eaf1f7
ffffff

Requirements
Must have
• I NEED MY LOGO AND LOGO OF DR VELTRONA

```html
<!DOCTYPE html>
<html lang="it">
<head>
<meta charset="utf-8">
<title>Veltrona – Business Card</title>
<link href="https://fonts.googleapis.com/css2?family=Montserrat:wght@400;600;700&display=swap" rel="stylesheet">
<style>
  :root{
    --sky:#33a6d7;
    --royal:#3176b5;
    --mist:#85abd2;
    --ice:#aedbee;
    --frost:#eaf1f7;
    --white:#ffffff;
    --ink:#3a3f47;
    --stage:#d9dee4;
  }
  *{margin:0;padding:0;box-sizing:border-box}
  html,body{width:1200px;height:675px;overflow:hidden}
  body{
    background:var(--stage);
    font-family:"Montserrat",Verdana,sans-serif;
    display:flex;align-items:center;justify-content:center;gap:60px;
  }
  .card{
    position:relative;width:520px;height:336px;border-radius:4px;overflow:hidden;
    box-shadow:0 18px 40px rgba(40,60,90,.22);
  }

  /* Front */
  .card--front{background:var(--white)}
  .card--front .accent{position:absolute;right:0;top:0;width:260px;height:336px}
  .brand{position:absolute;left:36px;top:40px;display:flex;align-items:center;gap:10px}
  .brand__dot{width:22px;height:22px;border-radius:50%;background:var(--royal)}
  .brand__name{font-weight:700;font-size:30px;color:var(--royal);letter-spacing:.5px}
  .brand__tagline{position:absolute;left:36px;top:80px;font-size:8.5px;font-weight:600;color:var(--royal);letter-spacing:.4px}
  .person{position:absolute;left:36px;top:150px}
  .person__name{font-size:22px;font-weight:400;color:var(--sky);letter-spacing:2px}
  .person__role{font-size:15px;color:var(--ink);margin-top:2px}
  .contacts{position:absolute;left:36px;top:224px;list-style:none}
  .contacts li{display:flex;align-items:center;gap:14px;font-size:15px;color:var(--ink);height:25px;letter-spacing:.4px}
  .contacts svg{width:14px;height:14px;flex:none}

  /* Back */
  .card--back{background:linear-gradient(135deg,var(--sky) 0%,#3aaede 55%,var(--sky) 100%)}
  .card--back .pill{position:absolute;left:0;top:0;width:520px;height:336px}
  .back-mark{position:absolute;left:46px;top:120px;width:96px;height:96px;border-radius:50%;background:var(--white)}
  .back-brand{position:absolute;left:232px;top:118px;color:var(--white)}
  .back-brand__name{font-weight:700;font-size:44px;letter-spacing:1px;line-height:1}
  .back-brand__tagline{font-size:10px;font-weight:600;letter-spacing:.5px;margin-top:6px}
  .web{position:absolute;left:0;right:0;bottom:30px;display:flex;justify-content:center;align-items:center;gap:10px;color:var(--white);font-size:15px;letter-spacing:1px}
  .web svg{width:15px;height:15px}
</style>
</head>
<body>

  <section class="card card--front">
    <svg class="accent" viewBox="0 0 260 336" aria-hidden="true">
      <defs>
        <linearGradient id="accentFill" x1="0" y1="0" x2="1" y2="1">
          <stop offset="0" stop-color="#aedbee"/>
          <stop offset="1" stop-color="#33a6d7"/>
        </linearGradient>
      </defs>
      <path d="M260 40 C170 60 130 150 150 336 L260 336 Z" fill="url(#accentFill)" opacity=".75"/>
      <path d="M60 0 C110 90 180 140 260 150 L260 175 C170 170 95 110 40 0 Z" fill="#3176b5"/>
    </svg>

    <div class="brand">
      <span class="brand__dot"></span>
      <span class="brand__name">Veltrona</span>
    </div>
    <p class="brand__tagline">CURA E REINTEGRAZIONE DEI CAPELLI</p>

    <div class="person">
      <h1 class="person__name">LUCA FERRANDI</h1>
      <p class="person__role">Hair Specialist</p>
    </div>

    <ul class="contacts">
      <li>
        <svg viewBox="0 0 24 24"><path d="M6.6 10.8a15 15 0 0 0 6.6 6.6l2.2-2.2a1 1 0 0 1 1-.25 11.4 11.4 0 0 0 3.6.57 1 1 0 0 1 1 1V20a1 1 0 0 1-1 1A17 17 0 0 1 3 4a1 1 0 0 1 1-1h3.5a1 1 0 0 1 1 1c0 1.25.2 2.45.57 3.57a1 1 0 0 1-.25 1z" fill="#33a6d7"/></svg>
        045 71 38 26
      </li>
      <li>
        <svg viewBox="0 0 24 24"><rect x="2" y="5" width="20" height="14" rx="1" fill="none" stroke="#33a6d7" stroke-width="2"/><path d="M2 6l10 7 10-7" fill="none" stroke="#33a6d7" stroke-width="2"/></svg>
        info@veltrona.it
      </li>
      <li>
        <svg viewBox="0 0 24 24"><path d="M12 2a7 7 0 0 0-7 7c0 5 7 13 7 13s7-8 7-13a7 7 0 0 0-7-7zm0 9.5A2.5 2.5 0 1 1 12 6.5a2.5 2.5 0 0 1 0 5z" fill="#33a6d7"/></svg>
        via Garibaldi 14 Verona
      </li>
    </ul>
  </section>

  <section class="card card--back">
    <svg class="pill" viewBox="0 0 520 336" aria-hidden="true">
      <path d="M540 90 H268 A78 78 0 0 0 268 246 H540" fill="none" stroke="#ffffff" stroke-width="14"/>
    </svg>
    <span class="back-mark"></span>
    <div class="back-brand">
      <h2 class="back-brand__name">Veltrona</h2>
      <p class="back-brand__tagline">CURA E REINTEGRAZIONE DEI CAPELLI</p>
    </div>
    <p class="web">
      <svg viewBox="0 0 24 24"><circle cx="12" cy="12" r="9" fill="none" stroke="#fff" stroke-width="2"/><path d="M3 12h18M12 3c3 3 3 15 0 18M12 3c-3 3-3 15 0 18" fill="none" stroke="#fff" stroke-width="1.6"/></svg>
      www.veltrona.it
    </p>
  </section>

</body>
</html>
```